Race car follow-up website needs web design

We are currently finalising a website which allows amateur and professional owners of race cars to track the running time of the car and all installed parts (drive shafts, gearbox etc.). The site is working for a technical point of view, but needs a nice design applied to it.

The website is made with Bootstrap 3.x and does not need a mobile skin. We target desktop and tablet users. This means that the delivered work should be easy to incorporate in the Bootstrap site that currently exists, from a technical point of view.

In attachment you can find all the screens that need skinning. If you think some stuff can be done better from a usability or design point of view (size of tables, placement of buttons etc.), do not hesitate to make a suggestion. We are open to positive criticism, and the current "base" design is not carved in stone. The colors currently used are basic Bootstrap so that can change too. There are no limits whatsoever, as long as the result looks good.

We have a big amount of racing/racecar/mechanic/pitbox related photo material that can be used, so do not hesitate to ask for material if needed.

The start page should be something along the lines of these sites:

https://plumvex.me/
http://quorvane.io/
https://teldrova.com/
http://www.mivostrel.com/

Or in words: a top navigation bar (as seen in the screenshots). A full-width image relevant to the content (racing related) with some text in overlay (A sort of slogan along the lines of "Let us track your parts" or "Parts tracking for you race or trackday car" ). Under that image there should then be a very high-level overview of what the website can be used for (In a few steps, with graphics/photos, schematics, showing driving the car, data transfer, management in the site.). This so the potential user can quickly see if it is of any interest to him/her.

Basically:

Drive --- Download data -- Get Alerted

each step should contain an "icon" representing what it is about, and a few lines of text explaining what is meant.

On that page (in the image part, or below the explanation) there should be 2 links (buttons). One leads to the pricing page, one to the registration page.

Of course this first page cannot be finalised until we give the complete details of the content, so please provide a high-level design and the person I work with will receive the detailed specs (the text for the different steps etc).

The other screens are (we think) self-explanatory. Please look at them in chronological order (they are prefixed 00 to 19)

There are screenshots of the manual. This page will also need to be styled (to match the rest of the site and to make the layout a bit more sexy). We will of course provide the original html file to this once the content needs to be finalised.

Besides the website, a mail template is required too. The site sends mails for:
- registration confirmation
- lost password
- alerts related to the car parts or the data files.

These mails should also have a professional looking skin (right now they are plain text)

Just to make things clear, if you think the base design we made is "crap", please suggest improvements (for instance, menu placement in the bottom, positioning of certain elements, tables that might be better off somewhere else, the car details on top that take too much screen real-estate etc. etc.). This site has been built by developers, not by designers. The only condition is that it should be technically possible in a reasonable amount of time using Bootstrap 3.x

Please provide the resources in such a way that a developer with web skills can directly implement them. So any slicing of graphics should be done by the designer. If you only provide us a good looking psd file we won't be able to do anything with that, unfortunately.

If you, as a designer, have a passion for sports cars, race cars, trackdays and/or GT car racing, this is of course a plus. The collaboration will be a lot easier if we speak the same "language".

Please provide at least a design of
- the start page
- the "car details" page
- one of the list modals
- one of the form modals

so we can at least know how the rest of the pages will look

The name is Pitlane Ledger.

Some pictures that can be used:

https://www.snapvelo.com/photos/58310472@K04/20581937466/
https://www.snapvelo.com/photos/58310472@K04/4815209367/
https://www.snapvelo.com/photos/58310472@K04/4812766058/
https://www.snapvelo.com/photos/58310472@K04/4801533729/
https://www.snapvelo.com/photos/58310472@K04/4763921850/
https://www.snapvelo.com/photos/58310472@K04/4706418592/
https://www.snapvelo.com/photos/58310472@K04/4594071683/
https://www.snapvelo.com/photos/58310472@K04/4361829074/
https://www.snapvelo.com/photos/58310472@K04/3958316247/
https://www.snapvelo.com/photos/58310472@K04/3927140568/
https://www.snapvelo.com/photos/58310472@K04/3915762839/
https://www.snapvelo.com/photos/58310472@K04/3915764901/
https://www.snapvelo.com/photos/58310472@K04/3890417352/
https://www.snapvelo.com/photos/58310472@K04/3885093716/
https://www.snapvelo.com/photos/58310472@K04/3885097284/
https://www.snapvelo.com/photos/58310472@K04/2081359647/
https://www.snapvelo.com/photos/58310472@K04/2398640513/
https://www.snapvelo.com/photos/58310472@K04/2486075129/
https://www.snapvelo.com/photos/58310472@K04/2323149876/
https://www.snapvelo.com/photos/58310472@K04/2323154902/

Basically you take whatever you want from this guy’s photo stream:
https://www.snapvelo.com/photos/58310472@K04/

I know him personally so there should be no copyright issues.

Most users of the site will run so called "GT" cars (Valdorni, Castruzzo etc.), so please refrain from using (or referencing) open wheelers, F1, LMP etc.

There is a logo contest too: http://gigs.pixelbazaar.com/gig.aspx?id=837461

I just updated the brief with some more info and images you can use.

I have updated the brief. This is added: for the first screen, the schematics are explained in a bit more detail: Basically: Drive ---> Download data --> Get Alerted each step should contain an "icon" representing what it is about, and a few lines of text explaining what is meant.

Dear designers, As we have received numerous remarks about our contest from you and your colleagues we have contacted PixelBazaar to solve the situation. This contest will be split into two different contests. One logo design contest for $400 and one website design contest for the $1480. Everyone who has submitted logos can of course participate with those logos in the logo design contest (there are a few that we like, which have been submitted). We are very sorry for the inconvenience we might have caused, and if you want to redraw your designs already submitted because of this we will fully understand this, but we hope this decision will make things clearer for everyone participating. As soon as matters are changed we will send you all a new message with the updated information. Thanks for your understanding. Morlek BVBA

The logo contest has been created: http://gigs.pixelbazaar.com/gig.aspx?id=837461

Reason: Because of the split in webdesign / logo the deadline has been extended so non-logo webdesigners can participate too. Logo project: http://gigs.pixelbazaar.com/gig.aspx?id=837461

The pricing page has been added in the screenshots section

Trackday enthousiasts, race car owners, race teams.

• No video
No huge "footer" with a lot of links to navigate the site, since there will be very litte content.
No references to non-GT type cars (so no F1, no Series Quelmont, no LMP1/LMP2) or street cars.

```html
<!DOCTYPE html>
<html lang="en">
<head>
<meta charset="utf-8">
<title>Pitlane Ledger — Let us track your parts</title>
<link rel="stylesheet" href="https://fonts.googleapis.com/css2?family=Domine:wght@400;700&family=Roboto:wght@300;400;500;700&display=swap">
<style>
  :root {
    --ink: #1f1f1f;
    --navy: #1d2a44;
    --gold: #c8b414;
    --red: #c40a0a;
    --band-1: #4c4c4c;
    --band-2: #444444;
    --band-3: #3a3a3a;
    --band-4: #2d2d2d;
    --muted: #6a6a6a;
    --serif: "Domine", Georgia, serif;
    --sans: "Roboto", Arial, sans-serif;
  }
  * { box-sizing: border-box; margin: 0; padding: 0; }
  html, body { width: 1200px; height: 1200px; overflow: hidden; }
  body {
    position: relative;
    font-family: var(--sans);
    color: var(--ink);
    background: radial-gradient(ellipse at 50% 30%, #ffffff 0%, #f2f2f2 55%, #e6e6e6 100%);
  }
  a { text-decoration: none; }
  .stripe {
    position: absolute; left: 0; width: 1200px; height: 4px;
    background: repeating-linear-gradient(90deg, var(--navy) 0 14px, transparent 14px 18px, #888 18px 30px, transparent 30px 34px);
  }
  .stripe--top { top: 0; }
  .stripe--bottom { top: 1110px; }

  /* header */
  .brand { position: absolute; display: flex; align-items: center; gap: 7px; }
  .brand__dot { width: 24px; height: 24px; border-radius: 50%; background: var(--gold); }
  .brand__name { font-family: var(--serif); font-size: 16px; color: #3a3a3a; letter-spacing: -0.3px; }
  .brand__badge {
    position: absolute; top: -12px; right: -6px;
    font: 700 7px var(--sans); color: #fff; background: var(--red);
    padding: 2px 3px; border-radius: 2px;
  }
  .brand--header { left: 216px; top: 28px; }
  .brand--footer { right: 218px; top: 1150px; }
  .brand--footer .brand__dot { background: #9a9a9a; }
  .brand--footer .brand__name { color: #7a7a7a; }
  .brand--footer .brand__badge { background: #6a6a6a; }

  .nav { position: absolute; left: 536px; top: 38px; display: flex; }
  .nav a {
    font: 500 9px var(--sans); color: var(--navy);
    letter-spacing: 0.4px; padding: 0 20px; border-left: 1px dotted #aaa;
  }
  .nav a:first-child { padding-left: 0; border-left: 0; }
  .btn {
    position: absolute; display: flex; align-items: center; justify-content: center;
    color: #fff; font-family: var(--sans); font-weight: 500;
  }
  .btn--gold { background: var(--gold); }
  .btn--red { background: var(--red); }
  .btn--sm { height: 25px; width: 61px; top: 30px; font-size: 9px; }

  /* hero */
  .hero__title {
    position: absolute; top: 108px; left: 0; width: 1200px; text-align: center;
    font: 400 40px var(--serif); letter-spacing: -2.5px; color: var(--ink);
  }
  .hero__title .red { color: var(--red); }
  .hero__title .gold { color: var(--gold); }
  .hero__lead {
    position: absolute; top: 154px; left: 0; width: 1200px; text-align: center;
    font: 400 9.5px var(--serif); color: var(--muted);
  }
  .hero__join {
    position: absolute; top: 174px; left: 0; width: 1200px; text-align: center;
    font: 400 16px var(--serif); color: #444;
  }
  .hero__chevron { position: absolute; left: 591px; top: 197px; }
  .hero__art {
    position: absolute; left: 200px; top: 228px; width: 1000px; height: 394px;
    background: radial-gradient(ellipse 60% 55% at 45% 50%, #1c1c1c 0%, #2a2a2a 45%, rgba(40,40,40,0.35) 75%, rgba(240,240,240,0) 100%);
  }

  /* features band */
  .features { position: absolute; left: 0; top: 622px; }
  .feature { position: absolute; top: 658px; text-align: right; }
  .feature__title { font: 400 21px var(--serif); color: var(--gold); line-height: 1; letter-spacing: -0.5px; }
  .feature__sub { font: 400 13px var(--serif); color: #e4e4e4; line-height: 1; margin-top: 1px; }
  .feature__icon { position: absolute; top: 712px; }

  /* about */
  .about__title {
    position: absolute; top: 855px; left: 0; width: 1200px; text-align: center;
    font: 400 38px var(--serif); letter-spacing: -2.5px;
  }
  .about__sub {
    position: absolute; top: 900px; left: 0; width: 1200px; text-align: center;
    font: 400 9.5px var(--serif); color: var(--muted); letter-spacing: 0.3px;
  }
  .about__text {
    position: absolute; top: 935px; left: 236px; width: 728px; text-align: center;
    font: 300 10.4px/16px var(--sans); color: #555;
  }
  .btn--lg { top: 1027px; height: 30px; width: 128px; font-size: 12px; }

  /* footer */
  .footer { position: absolute; left: 0; top: 1114px; width: 1200px; height: 86px;
    background: linear-gradient(#e3e3e3, #f6f6f6); }
  .footer__links { position: absolute; left: 216px; top: 1151px; font: 500 8.5px var(--sans); color: var(--navy); }
  .footer__links a { color: var(--navy); }
  .footer__copy { position: absolute; left: 216px; top: 1166px; font: 400 8px var(--sans); color: #888; }
  .footer__social { position: absolute; left: 565px; top: 1159px; display: flex; gap: 9px; }
  .footer__social a { width: 13px; height: 13px; border-radius: 50%; background: #555; display: block; }
</style>
</head>
<body>
  <div class="stripe stripe--top"></div>

  <header>
    <a class="brand brand--header" href="#">
      <span class="brand__dot"></span>
      <span class="brand__name">Pitlane Ledger</span>
      <span class="brand__badge">BETA</span>
    </a>
    <nav class="nav">
      <a href="#">HOME</a>
      <a href="#">REGISTER</a>
      <a href="#">MY CARS</a>
      <a href="#">CONTACT US</a>
    </nav>
    <a class="btn btn--gold btn--sm" style="left:856px" href="#">SIGN UP</a>
    <a class="btn btn--red btn--sm" style="left:921px" href="#">LOGIN</a>
  </header>

  <section class="hero">
    <h1 class="hero__title">LET US <span class="red">TRACK</span> <span class="gold">YOUR PARTS</span></h1>
    <p class="hero__lead">We Allows Amateur And Professional Owners Of Race Cars To Track The Running Time Of The Car And All Installed Parts</p>
    <p class="hero__join">JOIN US NOW!</p>
    <svg class="hero__chevron" width="18" height="18" viewBox="0 0 18 18" aria-hidden="true">
      <circle cx="9" cy="9" r="7.5" fill="none" stroke="#c40a0a" stroke-width="2"/>
      <path d="M5.5 7.5 L9 11 L12.5 7.5" fill="none" stroke="#c40a0a" stroke-width="2"/>
    </svg>
    <div class="hero__art" role="img" aria-label="Black GT supercar in three-quarter front view on a curved black road with yellow lane lines"></div>
  </section>

  <section class="features-wrap">
    <svg class="features" width="1200" height="193" viewBox="0 0 1200 193" aria-hidden="true">
      <polygon points="0,0 345,0 415,96 345,193 0,193" fill="var(--band-1)"/>
      <polygon points="345,0 572,0 637,96 572,193 345,193 415,96" fill="var(--band-2)"/>
      <polygon points="572,0 782,0 845,96 782,193 572,193 637,96" fill="var(--band-3)"/>
      <polygon points="782,0 985,0 1050,96 985,193 782,193 845,96" fill="var(--band-4)"/>
      <g fill="none" stroke="#555" stroke-width="1.5">
        <circle cx="382" cy="103" r="7"/><path d="M380 99 l4 4 -4 4"/>
        <circle cx="610" cy="103" r="7"/><path d="M608 99 l4 4 -4 4"/>
        <circle cx="817" cy="103" r="7"/><path d="M815 99 l4 4 -4 4"/>
        <circle cx="1024" cy="103" r="7"/><path d="M1022 99 l4 4 -4 4"/>
      </g>
    </svg>

    <div class="feature" style="right:852px">
      <div class="feature__title">KEEP TRACK</div>
      <div class="feature__sub">OF YOUR PARTS</div>
    </div>
    <div class="feature" style="right:631px">
      <div class="feature__title">KEEP TRACK</div>
      <div class="feature__sub">OF YOUR LAP TIMES</div>
    </div>
    <div class="feature" style="right:451px">
      <div class="feature__title">ALERTS</div>
      <div class="feature__sub">MESSAGES</div>
    </div>
    <div class="feature" style="right:219px">
      <div class="feature__title">YOUR CAR</div>
      <div class="feature__sub">FULE MILLAGE</div>
    </div>

    <svg class="feature__icon" style="left:245px" width="50" height="52" viewBox="0 0 50 52" aria-hidden="true">
      <g fill="none" stroke="#c8b414" stroke-width="2.5">
        <path d="M3 3 h44 v46 h-44 z"/>
        <path d="M12 12 h26 M12 19 h26 M12 26 h26 M12 33 h26 M12 40 h26"/>
      </g>
    </svg>
    <svg class="feature__icon" style="left:458px" width="56" height="56" viewBox="0 0 56 56" aria-hidden="true">
      <g fill="none" stroke="#c8b414" stroke-width="2.5">
        <circle cx="28" cy="28" r="25"/>
        <path d="M28 8 v5 M9 28 h5 M42 28 h5 M14 14 l3 3 M42 14 l-3 3 M15 42 l3-3 M41 42 l-3-3"/>
        <path d="M28 30 L42 20"/>
      </g>
      <circle cx="28" cy="30" r="4" fill="#c8b414"/>
    </svg>
    <svg class="feature__icon" style="left:675px" width="54" height="54" viewBox="0 0 54 54" aria-hidden="true">
      <g fill="none" stroke="#c8b414" stroke-width="2.5" stroke-linejoin="round">
        <path d="M3 22 L27 4 L51 22 V51 H3 Z"/>
        <path d="M10 16 V30 M44 16 V30 M10 16 H44"/>
        <path d="M3 22 L27 38 L51 22 M3 51 L21 34 M51 51 L33 34"/>
        <path d="M17 23 h20 M20 29 h14"/>
      </g>
    </svg>
    <svg class="feature__icon" style="left:900px" width="52" height="54" viewBox="0 0 52 54" aria-hidden="true">
      <g fill="none" stroke="#c8b414" stroke-width="2.5" stroke-linejoin="round">
        <path d="M4 51 V5 Q4 2 7 2 H29 Q32 2 32 5 V51"/>
        <path d="M1 51 H35"/>
        <path d="M9 8 H27 V22 H9 Z"/>
        <path d="M32 20 L40 24 Q45 28 45 36 V42 Q45 46 41 46 Q38 46 38 42 V32"/>
      </g>
    </svg>
  </section>

  <section class="about">
    <h2 class="about__title">WHO WE ARE?</h2>
    <p class="about__sub">WHAT IS THIS SITE ABOUT</p>
    <p class="about__text">As most people involved in racing or track days already know, it is very important to closely follow up the number of operationg hours of different parts of your car ( e.g. drive shafts, gear box, engine ) in order ot avoid mechanical breakdowns and accidents. Up untill now this usually done manually, either by writing down the number of opertation hours after each race weekend and the install dates of different parts, or even worsem by "estimating" the amount of hours by looking at the number of days the car was used.</p>
    <a class="btn btn--gold btn--lg" style="left:456px" href="#">REGISTERED NOW</a>
    <a class="btn btn--red btn--lg" style="left:595px" href="#">PRICING</a>
  </section>

  <div class="stripe stripe--bottom"></div>
  <footer class="footer"></footer>
  <div class="footer__links"><a href="#">HOME</a> - <a href="#">REGISTER</a> - <a href="#">MY CARS</a> - <a href="#">CONTACT US</a></div>
  <div class="footer__copy">Copyright © PITLANELEDGER. All Right Reserved.</div>
  <div class="footer__social">
    <a href="#" aria-label="Social link 1"></a>
    <a href="#" aria-label="Social link 2"></a>
    <a href="#" aria-label="Social link 3"></a>
    <a href="#" aria-label="Social link 4"></a>
  </div>
  <a class="brand brand--footer" href="#">
    <span class="brand__dot"></span>
    <span class="brand__name">Pitlane Ledger</span>
    <span class="brand__badge">BETA</span>
  </a>
</body>
</html>
```